FUN Sizing Chart for Apparel Company.

We are a company called GROAN, we make cycling jerseys for the fun lovers and beer enthusiasts.....they might even like to bike. www.groankitvale.com We need a nice looking, but more importantly fun sizing chart created that reflects our personality. I've attached the sizing provided by the manufacturer with some information omitted --- what they provided was overkill and confusing, we just need chest measurements. Please create the graphic so that we can somewhat easily adjust the measurements should our pattern change.

FUN is the big winner. Our brand represents light-heartedness. For example, we chose to size our jerseys in volumes of beer which may or may not be incorporated into the graphic:
X-Small = The Half-Pint
Small = The Pint
Medium = The Bomber
Large = The Forty
X-Large = The Growler
XX-Large = The Pony Keg
XXX-Large = The Keg

Industry/Entity Type

It Company

```html
<!DOCTYPE html>
<html lang="en">
<head>
<meta charset="utf-8">
<title>GROAN Jersey Sizing Chart</title>
<link rel="stylesheet" href="https://fonts.googleapis.com/css2?family=Archivo+Black&family=Oswald:wght@500;700&family=Roboto+Mono&display=swap">
<style>
  :root {
    --mint: #c3f9dc;
    --band-male: #ffffff;
    --band-female: #e4fcef;
    --wordmark: #ffffff;
    --vessel-name: #a7a8a6;
    --label-ink: #3a3a3a;
    --number-ink: #454545;
    --row-key: #8e8e8e;
    --beer: #ff6600;
    --beer-deep: #f05a00;
    --glass-edge: #4a4a4a;
    --foam: #f4f4f4;
    --ground: #b9cfc2;
  }
  * { margin: 0; padding: 0; box-sizing: border-box; }
  html, body { width: 1200px; height: 450px; overflow: hidden; background: var(--mint); }
  .chart { position: relative; width: 1200px; height: 450px; background: var(--mint); overflow: hidden; }

  .brand-wordmark {
    position: absolute; left: 150px; top: -14px;
    font-family: "Archivo Black", sans-serif; font-size: 124px; line-height: 1;
    color: var(--wordmark); letter-spacing: -2px;
  }
  .brand-tag {
    position: absolute; left: 700px; top: 6px;
    writing-mode: vertical-rl;
    font-family: "Roboto Mono", monospace; font-size: 10px; letter-spacing: 5px;
    color: var(--wordmark);
  }

  .ground-line { position: absolute; left: 95px; top: 307px; width: 1060px; height: 1px; background: var(--ground); }

  .vessel {
    position: absolute;
    background: linear-gradient(180deg, var(--beer) 0%, var(--beer-deep) 100%);
    border: 4px solid var(--glass-edge);
    border-top-width: 14px;
    border-top-color: var(--foam);
  }

  .vessel-name {
    position: absolute; bottom: 138px;
    writing-mode: vertical-rl; transform: rotate(180deg);
    font-family: "Oswald", sans-serif; font-weight: 700; font-size: 35px; line-height: 1;
    color: var(--vessel-name); letter-spacing: 0.5px; white-space: nowrap;
  }

  .size-label {
    position: absolute; top: 332px; transform: translateX(-50%);
    font-family: "Oswald", sans-serif; font-weight: 700; font-size: 13px;
    color: var(--label-ink); white-space: nowrap;
  }

  .measure-band { position: absolute; left: 30px; width: 1170px; }
  .measure-band.male { top: 367px; height: 23px; background: var(--band-male); }
  .measure-band.female { top: 398px; height: 19px; background: var(--band-female); }

  .row-key {
    position: absolute; left: 14px;
    font-family: "Oswald", sans-serif; font-weight: 700; font-size: 24px; line-height: 1;
    color: var(--row-key);
  }
  .row-key.male { top: 364px; }
  .row-key.female { top: 396px; }

  .measure {
    position: absolute; transform: translateX(-50%);
    font-family: "Roboto Mono", monospace; font-size: 20px; line-height: 1;
    color: var(--number-ink);
  }
  .measure.male { top: 368px; }
  .measure.female { top: 400px; }
</style>
</head>
<body>
<main class="chart">
  <div class="brand-wordmark">GROAN</div>
  <div class="brand-tag">SIZING</div>

  <div class="ground-line"></div>

  <div class="vessel" role="img" aria-label="Cheerful cartoon half-pint glass of beer character waving its arms" style="left:62px;top:186px;width:50px;height:126px;border-radius:10px 10px 12px 12px;"></div>
  <div class="vessel" role="img" aria-label="Cheerful cartoon pint mug of beer character waving its arms" style="left:178px;top:186px;width:120px;height:128px;border-radius:40px 40px 30px 30px;"></div>
  <div class="vessel" role="img" aria-label="Cheerful cartoon bomber glass of beer character waving its arms" style="left:342px;top:162px;width:88px;height:152px;border-radius:14px 14px 24px 24px;"></div>
  <div class="vessel" role="img" aria-label="Cheerful cartoon forty mug of beer character waving its arms" style="left:486px;top:140px;width:120px;height:172px;border-radius:18px 18px 20px 20px;"></div>
  <div class="vessel" role="img" aria-label="Cheerful cartoon growler jug of beer character waving its arms" style="left:652px;top:106px;width:94px;height:214px;border-radius:40px 40px 36px 36px;"></div>
  <div class="vessel" role="img" aria-label="Cheerful cartoon pony keg of beer character waving its arms" style="left:800px;top:115px;width:146px;height:200px;border-radius:30px 30px 24px 24px;"></div>
  <div class="vessel" role="img" aria-label="Cheerful cartoon keg of beer character waving its arms" style="left:988px;top:85px;width:150px;height:230px;border-radius:30px 30px 24px 24px;"></div>

  <div class="vessel-name" style="left:116px;">THE HALF-PINT</div>
  <div class="vessel-name" style="left:302px;">THE PINT</div>
  <div class="vessel-name" style="left:434px;">THE BOMBER</div>
  <div class="vessel-name" style="left:610px;">THE FORTY</div>
  <div class="vessel-name" style="left:751px;">THE GROWLER</div>
  <div class="vessel-name" style="left:949px;">THE PONY KEG</div>
  <div class="vessel-name" style="left:1143px;">THE KEG</div>

  <div class="size-label" style="left:86px;">X-SMALL</div>
  <div class="size-label" style="left:228px;top:334px;">SMALL</div>
  <div class="size-label" style="left:388px;">MEDIUM</div>
  <div class="size-label" style="left:540px;">LARGE</div>
  <div class="size-label" style="left:700px;">X-LARGE</div>
  <div class="size-label" style="left:862px;">XX-LARGE</div>
  <div class="size-label" style="left:1060px;">XXX-LARGE</div>

  <div class="measure-band male"></div>
  <div class="measure-band female"></div>
  <div class="row-key male">M</div>
  <div class="row-key female">F</div>

  <span class="measure male" style="left:228px;">40</span>
  <span class="measure male" style="left:397px;">42.5</span>
  <span class="measure male" style="left:540px;">45</span>
  <span class="measure male" style="left:700px;">47.5</span>
  <span class="measure male" style="left:862px;">50</span>
  <span class="measure male" style="left:1060px;">52.5</span>

  <span class="measure female" style="left:84px;">34</span>
  <span class="measure female" style="left:228px;">36</span>
  <span class="measure female" style="left:382px;">38</span>
  <span class="measure female" style="left:540px;">40</span>
  <span class="measure female" style="left:700px;">42.5</span>
  <span class="measure female" style="left:862px;">45</span>
</main>
</body>
</html>
```